TEEVO LINKS KIT has a new golf related product called the fairwisp ball holder.clips onto your belt

TEEVO LINKS KITS new product is called the FAIRWISP BALL HOLDER..it is a small injection molded product that clips onto your belt or waistline and holds one golf ball.Being a canadian product it has to have french and english to correspond with government packaging regulations.
This is the information that needs to be on the package...that it is a product by teevo links kit...whose slogan is "kit to tidy your round"..it comes in 5 colors....black..orange..lime green...blue and pink...it weighs only 2 oz..web...is www.teevolinkskit.example...email..teevolinkskit@mailbox.example..that it clips onto your belt or waistlband...made in china for teevolinks kit britishcolumbia canada...patent pending..that it is for all golfers at all level of experience.includes drawstring storage bag..ball holder.made of polypropelene....on the back an idea is to have a picture of a person holding a golf club with a fairwisp ball holder clipped onto his or her belt

Target Market(s)

golfers of all ages....more towards women...and seniors

Industry/Entity Type

Government

Requirements
Must have
• bold noticable colors....must be eye catching...not to cluttered on the front...just bullet points....must have french....premium quality appeal...teevo links kit logo
• colors should relate to the colors of the product
Nice to have
• english...french and spanish
Should not have
• no more than 4 colors maximum

```html
<!DOCTYPE html>
<html lang="en">
<head>
<meta charset="utf-8">
<title>Fairwisp Ball Holder – Packaging Cards</title>
<link href="https://fonts.googleapis.com/css2?family=Roboto+Condensed:wght@700;800&family=Open+Sans:wght@300;400;700&display=swap" rel="stylesheet">
<style>
  :root{
    --sky:#a9c7e2;
    --field:#4f8a3c;
    --ink:#111;
    --white:#fff;
    --box-fill:#c4c4c4;
    --blue:#1f6fa6;
    --orange:#f29a2e;
    --pink:#f0a0b0;
    --green:#1f7a3a;
    --black:#1a1a1a;
    --sw-black:#000;
    --sw-orange:#f7a21b;
    --sw-lime:#8dc63f;
    --sw-blue:#1ba1e2;
    --sw-pink:#f49ac1;
    --photo-sky:#5d9bd8;
    --photo-grass:#4f8f3a;
  }
  *{box-sizing:border-box;margin:0;padding:0}
  html,body{width:1200px;height:975px;overflow:hidden;background:var(--white)}
  body{position:relative;font-family:"Open Sans",Arial,sans-serif;color:var(--ink)}

  .card{position:absolute;width:390px;height:470px;border-radius:20px;overflow:hidden;
    background:linear-gradient(180deg,var(--sky) 0%,var(--sky) 42%,#8fb0a8 62%,var(--field) 100%)}
  .card--blue{left:8px;top:12px;--accent:var(--blue)}
  .card--orange{left:405px;top:12px;--accent:var(--orange)}
  .card--pink{left:803px;top:12px;--accent:var(--pink)}
  .card--green{left:8px;top:492px;--accent:var(--green)}
  .card--black{left:405px;top:492px;--accent:var(--black)}
  .card--back{left:803px;top:492px}

  .card__art{position:absolute;inset:0}
  .band{fill:var(--accent)}
  .hang-hole{position:absolute;left:145px;top:10px;width:100px;height:28px;border-radius:14px;background:var(--white)}

  .brand{position:absolute;left:14px;top:22px;display:flex;flex-direction:column;align-items:flex-start;gap:3px}
  .brand__dot{width:18px;height:18px;border-radius:50%;background:var(--ink)}
  .brand__name{font-size:8px;font-weight:400;color:var(--ink)}

  .title{position:absolute;left:55px;top:62px;width:280px;text-align:center;
    font-family:"Roboto Condensed","Arial Narrow",sans-serif;font-weight:800;font-size:44px;
    color:var(--accent);-webkit-text-stroke:1px rgba(0,0,0,.55);line-height:1}
  .subtitle{position:absolute;left:40px;top:133px;width:305px;text-align:center;
    font-family:"Roboto Condensed","Arial Narrow",sans-serif;font-weight:700;font-size:24px;line-height:1;
    padding-bottom:4px;border-bottom:2px solid var(--ink)}
  .tagline{position:absolute;left:30px;top:168px;width:340px;font-size:17px;font-weight:300;white-space:nowrap}

  .includes{position:absolute;left:18px;top:204px;font-size:8px;font-weight:700;line-height:10.5px}
  .includes h4{font-size:8px;font-weight:700;margin-left:8px}
  .includes ul{list-style:none;margin-bottom:5px}
  .includes li::before{content:"•";margin-right:4px}

  .colours{position:absolute;left:270px;top:268px;width:112px;font-size:8px;font-weight:700;line-height:10.5px}
  .colours h4{font-size:7.5px;font-weight:700;margin-bottom:3px;white-space:nowrap}
  .colours ul{list-style:none;margin:0 0 13px 22px}
  .colours li{display:flex;justify-content:space-between;align-items:center}
  .swatch{width:8px;height:8px}
  .sw-black{background:var(--sw-black)}.sw-orange{background:var(--sw-orange)}
  .sw-lime{background:var(--sw-lime)}.sw-blue{background:var(--sw-blue)}.sw-pink{background:var(--sw-pink)}

  .weight{position:absolute;left:30px;top:434px;font-size:13px;font-weight:700;white-space:nowrap}
  .contact{position:absolute;right:14px;top:429px;text-align:right;font-size:8px;font-weight:700;line-height:15px;white-space:nowrap}

  .back__photo{position:absolute;inset:0;
    background:linear-gradient(180deg,var(--photo-sky) 0%,#9cc4ea 70%,var(--photo-grass) 100%)}
  .back__figure{position:absolute;left:215px;top:0;width:175px;height:470px;
    background:linear-gradient(180deg,rgba(156,122,184,0) 0%,rgba(156,122,184,.55) 40%,rgba(156,122,184,.25) 100%)}
  .back__window{position:absolute;left:105px;top:62px;width:178px;height:176px;background:var(--white)}
  .back__brand{position:absolute;left:22px;top:382px;display:flex;flex-direction:column;gap:4px}
  .back__brand .brand__dot{width:30px;height:30px;margin-left:20px}
  .back__brand .brand__name{font-size:11px}
  .back__slogan{font-size:7.5px;font-weight:700}
  .made-in{position:absolute;right:18px;top:395px;font-size:10px;font-weight:700}
</style>
</head>
<body>

<section class="card card--blue" aria-label="Fairwisp front, blue">
  <svg class="card__art" viewBox="0 0 390 470" aria-hidden="true">
    <path class="band" d="M300,0 L390,0 L390,60 C250,180 140,330 90,470 L0,470 L0,430 C90,300 200,130 300,0 Z"/>
    <path d="M390,72 C258,190 150,330 102,470 L94,470 C142,328 250,184 390,62 Z" fill="#fff" opacity=".35"/>
    <path d="M0,455 C50,380 110,300 180,230 C120,310 60,390 20,470 L0,470 Z" fill="#000"/>
    <path d="M50,55 L340,55 L325,118 L65,118 Z" fill="#fff" stroke="#000" stroke-width="3"/>
    <path d="M58,61 L332,61 L319,112 L71,112 Z" fill="#c4c4c4"/>
    <path d="M140,258 H248 V345 L232,430 H156 L140,345 Z" fill="#fff" stroke="#555" stroke-width=".6"/>
  </svg>
  <div class="hang-hole"></div>
  <div class="brand"><span class="brand__dot"></span><span class="brand__name">TEEVO LINKS KIT</span></div>
  <h1 class="title">FAIRWISP</h1>
  <h2 class="subtitle">BALL HOLDER</h2>
  <p class="tagline">For all golfers at all level of experience</p>
  <div class="includes">
    <h4>Includes:</h4>
    <ul><li>Drawstring storage bag</li><li>Ball holder</li></ul>
    <h4>Comprend:</h4>
    <ul><li>Cordon sac de rangement</li><li>Support de balle</li></ul>
  </div>
  <div class="colours">
    <h4>Product by TEEVO LINKS KIT</h4>
    <ul><li>Black<span class="swatch sw-black"></span></li><li>Orange<span class="swatch sw-orange"></span></li><li>LimeGreen<span class="swatch sw-lime"></span></li><li>Blue<span class="swatch sw-blue"></span></li><li>Pink<span class="swatch sw-pink"></span></li></ul>
    <h4>Produit par TEEVO LINKS KIT</h4>
    <ul><li>Noir<span class="swatch sw-black"></span></li><li>Orange<span class="swatch sw-orange"></span></li><li>Vert lime<span class="swatch sw-lime"></span></li><li>Bleu<span class="swatch sw-blue"></span></li><li>Rose<span class="swatch sw-pink"></span></li></ul>
  </div>
  <p class="weight">Weight:&nbsp; 2oz</p>
  <p class="contact">www.teevolinkskit.example<br>teevolinkskit@mailbox.example</p>
</section>

<section class="card card--orange" aria-label="Fairwisp front, orange">
  <svg class="card__art" viewBox="0 0 390 470" aria-hidden="true">
    <path class="band" d="M300,0 L390,0 L390,60 C250,180 140,330 90,470 L0,470 L0,430 C90,300 200,130 300,0 Z"/>
    <path d="M390,72 C258,190 150,330 102,470 L94,470 C142,328 250,184 390,62 Z" fill="#fff" opacity=".35"/>
    <path d="M0,455 C50,380 110,300 180,230 C120,310 60,390 20,470 L0,470 Z" fill="#000"/>
    <path d="M50,55 L340,55 L325,118 L65,118 Z" fill="#fff" stroke="#000" stroke-width="3"/>
    <path d="M58,61 L332,61 L319,112 L71,112 Z" fill="#c4c4c4"/>
    <path d="M140,258 H248 V345 L232,430 H156 L140,345 Z" fill="#fff" stroke="#555" stroke-width=".6"/>
  </svg>
  <div class="hang-hole"></div>
  <div class="brand"><span class="brand__dot"></span><span class="brand__name">TEEVO LINKS KIT</span></div>
  <h1 class="title">FAIRWISP</h1>
  <h2 class="subtitle">BALL HOLDER</h2>
  <p class="tagline">For all golfers at all level of experience</p>
  <div class="includes">
    <h4>Includes:</h4>
    <ul><li>Drawstring storage bag</li><li>Ball holder</li></ul>
    <h4>Comprend:</h4>
    <ul><li>Cordon sac de rangement</li><li>Support de balle</li></ul>
  </div>
  <div class="colours">
    <h4>Product by TEEVO LINKS KIT</h4>
    <ul><li>Black<span class="swatch sw-black"></span></li><li>Orange<span class="swatch sw-orange"></span></li><li>LimeGreen<span class="swatch sw-lime"></span></li><li>Blue<span class="swatch sw-blue"></span></li><li>Pink<span class="swatch sw-pink"></span></li></ul>
    <h4>Produit par TEEVO LINKS KIT</h4>
    <ul><li>Noir<span class="swatch sw-black"></span></li><li>Orange<span class="swatch sw-orange"></span></li><li>Vert lime<span class="swatch sw-lime"></span></li><li>Bleu<span class="swatch sw-blue"></span></li><li>Rose<span class="swatch sw-pink"></span></li></ul>
  </div>
  <p class="weight">Weight:&nbsp; 2oz</p>
  <p class="contact">www.teevolinkskit.example<br>teevolinkskit@mailbox.example</p>
</section>

<section class="card card--pink" aria-label="Fairwisp front, pink">
  <svg class="card__art" viewBox="0 0 390 470" aria-hidden="true">
    <path class="band" d="M300,0 L390,0 L390,60 C250,180 140,330 90,470 L0,470 L0,430 C90,300 200,130 300,0 Z"/>
    <path d="M390,72 C258,190 150,330 102,470 L94,470 C142,328 250,184 390,62 Z" fill="#fff" opacity=".35"/>
    <path d="M0,455 C50,380 110,300 180,230 C120,310 60,390 20,470 L0,470 Z" fill="#000"/>
    <path d="M50,55 L340,55 L325,118 L65,118 Z" fill="#fff" stroke="#000" stroke-width="3"/>
    <path d="M58,61 L332,61 L319,112 L71,112 Z" fill="#c4c4c4"/>
    <path d="M140,258 H248 V345 L232,430 H156 L140,345 Z" fill="#fff" stroke="#555" stroke-width=".6"/>
  </svg>
  <div class="hang-hole"></div>
  <div class="brand"><span class="brand__dot"></span><span class="brand__name">TEEVO LINKS KIT</span></div>
  <h1 class="title">FAIRWISP</h1>
  <h2 class="subtitle">BALL HOLDER</h2>
  <p class="tagline">For all golfers at all level of experience</p>
  <div class="includes">
    <h4>Includes:</h4>
    <ul><li>Drawstring storage bag</li><li>Ball holder</li></ul>
    <h4>Comprend:</h4>
    <ul><li>Cordon sac de rangement</li><li>Support de balle</li></ul>
  </div>
  <div class="colours">
    <h4>Product by TEEVO LINKS KIT</h4>
    <ul><li>Black<span class="swatch sw-black"></span></li><li>Orange<span class="swatch sw-orange"></span></li><li>LimeGreen<span class="swatch sw-lime"></span></li><li>Blue<span class="swatch sw-blue"></span></li><li>Pink<span class="swatch sw-pink"></span></li></ul>
    <h4>Produit par TEEVO LINKS KIT</h4>
    <ul><li>Noir<span class="swatch sw-black"></span></li><li>Orange<span class="swatch sw-orange"></span></li><li>Vert lime<span class="swatch sw-lime"></span></li><li>Bleu<span class="swatch sw-blue"></span></li><li>Rose<span class="swatch sw-pink"></span></li></ul>
  </div>
  <p class="weight">Weight:&nbsp; 2oz</p>
  <p class="contact">www.teevolinkskit.example<br>teevolinkskit@mailbox.example</p>
</section>

<section class="card card--green" aria-label="Fairwisp front, green">
  <svg class="card__art" viewBox="0 0 390 470" aria-hidden="true">
    <path class="band" d="M300,0 L390,0 L390,60 C250,180 140,330 90,470 L0,470 L0,430 C90,300 200,130 300,0 Z"/>
    <path d="M390,72 C258,190 150,330 102,470 L94,470 C142,328 250,184 390,62 Z" fill="#fff" opacity=".35"/>
    <path d="M0,455 C50,380 110,300 180,230 C120,310 60,390 20,470 L0,470 Z" fill="#000"/>
    <path d="M50,55 L340,55 L325,118 L65,118 Z" fill="#fff" stroke="#000" stroke-width="3"/>
    <path d="M58,61 L332,61 L319,112 L71,112 Z" fill="#c4c4c4"/>
    <path d="M140,258 H248 V345 L232,430 H156 L140,345 Z" fill="#fff" stroke="#555" stroke-width=".6"/>
  </svg>
  <div class="hang-hole"></div>
  <div class="brand"><span class="brand__dot"></span><span class="brand__name">TEEVO LINKS KIT</span></div>
  <h1 class="title">FAIRWISP</h1>
  <h2 class="subtitle">BALL HOLDER</h2>
  <p class="tagline">For all golfers at all level of experience</p>
  <div class="includes">
    <h4>Includes:</h4>
    <ul><li>Drawstring storage bag</li><li>Ball holder</li></ul>
    <h4>Comprend:</h4>
    <ul><li>Cordon sac de rangement</li><li>Support de balle</li></ul>
  </div>
  <div class="colours">
    <h4>Product by TEEVO LINKS KIT</h4>
    <ul><li>Black<span class="swatch sw-black"></span></li><li>Orange<span class="swatch sw-orange"></span></li><li>LimeGreen<span class="swatch sw-lime"></span></li><li>Blue<span class="swatch sw-blue"></span></li><li>Pink<span class="swatch sw-pink"></span></li></ul>
    <h4>Produit par TEEVO LINKS KIT</h4>
    <ul><li>Noir<span class="swatch sw-black"></span></li><li>Orange<span class="swatch sw-orange"></span></li><li>Vert lime<span class="swatch sw-lime"></span></li><li>Bleu<span class="swatch sw-blue"></span></li><li>Rose<span class="swatch sw-pink"></span></li></ul>
  </div>
  <p class="weight">Weight:&nbsp; 2oz</p>
  <p class="contact">www.teevolinkskit.example<br>teevolinkskit@mailbox.example</p>
</section>

<section class="card card--black" aria-label="Fairwisp front, black">
  <svg class="card__art" viewBox="0 0 390 470" aria-hidden="true">
    <defs>
      <linearGradient id="band-black" gradientUnits="userSpaceOnUse" x1="150" y1="0" x2="390" y2="0">
        <stop offset="0" stop-color="#a0a0a0"/>
        <stop offset=".45" stop-color="#7a7a7a"/>
        <stop offset="1" stop-color="#111"/>
      </linearGradient>
    </defs>
    <path d="M300,0 L390,0 L390,60 C250,180 140,330 90,470 L0,470 L0,430 C90,300 200,130 300,0 Z" fill="url(#band-black)"/>
    <path d="M390,72 C258,190 150,330 102,470 L94,470 C142,328 250,184 390,62 Z" fill="#fff" opacity=".35"/>
    <path d="M0,455 C50,380 110,300 180,230 C120,310 60,390 20,470 L0,470 Z" fill="#000"/>
    <path d="M50,55 L340,55 L325,118 L65,118 Z" fill="#fff" stroke="#000" stroke-width="3"/>
    <path d="M58,61 L332,61 L319,112 L71,112 Z" fill="#c4c4c4"/>
    <path d="M140,258 H248 V345 L232,430 H156 L140,345 Z" fill="#fff" stroke="#555" stroke-width=".6"/>
  </svg>
  <div class="hang-hole"></div>
  <div class="brand"><span class="brand__dot"></span><span class="brand__name">TEEVO LINKS KIT</span></div>
  <h1 class="title">FAIRWISP</h1>
  <h2 class="subtitle">BALL HOLDER</h2>
  <p class="tagline">For all golfers at all level of experience</p>
  <div class="includes">
    <h4>Includes:</h4>
    <ul><li>Drawstring storage bag</li><li>Ball holder</li></ul>
    <h4>Comprend:</h4>
    <ul><li>Cordon sac de rangement</li><li>Support de balle</li></ul>
  </div>
  <div class="colours">
    <h4>Product by TEEVO LINKS KIT</h4>
    <ul><li>Black<span class="swatch sw-black"></span></li><li>Orange<span class="swatch sw-orange"></span></li><li>LimeGreen<span class="swatch sw-lime"></span></li><li>Blue<span class="swatch sw-blue"></span></li><li>Pink<span class="swatch sw-pink"></span></li></ul>
    <h4>Produit par TEEVO LINKS KIT</h4>
    <ul><li>Noir<span class="swatch sw-black"></span></li><li>Orange<span class="swatch sw-orange"></span></li><li>Vert lime<span class="swatch sw-lime"></span></li><li>Bleu<span class="swatch sw-blue"></span></li><li>Rose<span class="swatch sw-pink"></span></li></ul>
  </div>
  <p class="weight">Weight:&nbsp; 2oz</p>
  <p class="contact">www.teevolinkskit.example<br>teevolinkskit@mailbox.example</p>
</section>

<section class="card card--back" aria-label="Fairwisp back">
  <div class="back__photo" role="img" aria-label="Photo of a golfer mid-swing on a course with a ball holder clipped to the belt">
    <div class="back__figure"></div>
  </div>
  <div class="hang-hole"></div>
  <div class="back__window"></div>
  <svg class="card__art" viewBox="0 0 390 470" aria-hidden="true">
    <path d="M140,258 H248 V345 L232,430 H156 L140,345 Z" fill="#fff" stroke="#555" stroke-width=".6"/>
  </svg>
  <div class="back__brand">
    <span class="brand__dot"></span>
    <span class="brand__name">TEEVO LINKS KIT</span>
    <span class="back__slogan">Kit to Tidy Your Round</span>
  </div>
  <p class="made-in">Made in China</p>
</section>

</body>
</html>
```